Apex Game Photo Matching

I’m looking for an elite classy website where it talks a little bit about my experience and a video page and updates once a week of items I photo matched. I would like you to look at my three competitors for ideas on their sites I like them all. I photo match all professional sports game used equipment to the actual game they used it in.

```html
<!DOCTYPE html>
<html lang="en">
<head>
<meta charset="utf-8">
<title>Apex Game Photo Matching</title>
<link rel="stylesheet" href="https://fonts.googleapis.com/css2?family=Titillium+Web:wght@300;400;600;700;900&family=Roboto+Condensed:wght@400;700&family=Lato:wght@400;700;900&display=swap">
<style>
:root{
  --blue:#1f4fa8;
  --blue-bright:#2a8fd6;
  --ink:#1b1b1b;
  --text:#3a3a3a;
  --muted:#6b6b6b;
  --gray-band:#eeeeee;
  --dark:#161616;
  --footer:#1a1a1a;
  --white:#ffffff;
  --play:rgba(20,20,20,.75);
}
*{box-sizing:border-box;margin:0;padding:0}
html,body{width:1200px;height:4515px;overflow:hidden}
body{position:relative;background:var(--white);font-family:"Lato",sans-serif;color:var(--text)}
.abs{position:absolute}
.heading{font-family:"Titillium Web",sans-serif;color:var(--ink)}

/* hero */
.hero{left:0;top:0;width:1200px;height:739px;
  background:radial-gradient(ellipse at 55% 35%,#4a5b70 0%,#26303d 40%,#10161d 75%),#10161d;}
.hero-photo{left:0;top:0;width:1200px;height:739px;
  background:linear-gradient(180deg,rgba(20,28,40,.2) 0%,rgba(20,28,40,0) 55%,rgba(40,70,40,.55) 85%,rgba(30,50,30,.8) 100%);}
.brand{left:144px;top:70px;font-family:"Titillium Web",sans-serif;font-weight:900;font-size:40px;color:var(--white);letter-spacing:1px;display:flex;align-items:center;gap:12px}
.brand .mark{width:34px;height:34px;border-radius:50%;background:var(--white)}
.call{left:646px;top:34px;display:flex;align-items:center;gap:10px;font-family:"Roboto Condensed",sans-serif;color:var(--white);font-size:20px;white-space:nowrap}
.membership{left:920px;top:28px;width:135px;height:37px;border-radius:19px;background:var(--blue);color:var(--white);font-family:"Lato",sans-serif;font-weight:900;font-size:13px;display:flex;align-items:center;justify-content:center;letter-spacing:.5px}
.nav{left:520px;top:106px;width:536px;display:flex;justify-content:space-between;font-family:"Roboto Condensed",sans-serif;font-weight:700;font-size:14px;color:var(--white);text-transform:uppercase}
.nav .active{color:#6aa6ff}
.nav-rule{left:520px;top:144px;width:536px;height:1px;background:rgba(255,255,255,.25)}
.hero-title{left:0;width:1200px;text-align:center;color:var(--white);font-family:"Titillium Web",sans-serif}
.hero-title.light{top:320px;font-weight:400;font-size:66px;line-height:1}
.hero-title.bold{top:390px;font-weight:900;font-size:68px;line-height:1;letter-spacing:-1px}
.btn-pill{border-radius:22px;background:var(--blue);color:var(--white);font-weight:900;font-family:"Lato",sans-serif;display:flex;align-items:center;justify-content:center;text-transform:uppercase}
.hero-btn{left:512px;top:494px;width:175px;height:42px;font-size:15px}
.dots{left:566px;top:691px;display:flex;gap:5px}
.dots span{width:13px;height:13px;border-radius:50%;border:2px solid var(--white)}
.dots span.on{background:var(--blue-bright);border-color:var(--blue-bright)}

/* welcome */
.welcome-kicker{left:144px;top:825px;font-weight:300;font-size:38px;line-height:1}
.welcome-title{left:144px;top:867px;font-weight:700;font-size:36px;line-height:1}
.bar{height:4px;background:var(--blue);width:64px}
.welcome-bar{left:144px;top:928px}
.welcome-text{left:144px;top:956px;width:440px;font-size:14.5px;line-height:24px;color:var(--text)}
.welcome-btn{left:144px;top:1197px;width:151px;height:37px;font-size:13px}
.hex{left:669px;top:823px;width:387px;height:445px;clip-path:polygon(50% 0,100% 25%,100% 75%,50% 100%,0 75%,0 25%);
  background:radial-gradient(circle at 55% 40%,#7f9bb0 0%,#3b5470 35%,#0e1c2c 80%)}

/* photo matching */
.gray-band{left:0;top:1331px;width:1200px;height:722px;background:var(--gray-band)}
.notch{left:762px;top:1331px;width:198px;height:53px;background:var(--white);clip-path:polygon(0 0,100% 0,50% 100%)}
.section-title{left:0;width:1200px;text-align:center;font-weight:700;font-size:37px;line-height:1}
.center-bar{left:568px}
.pm-sub{left:0;top:1492px;width:1200px;text-align:center;font-size:14px;color:var(--text)}
.match-card{width:286px;top:1550px}
.match-img{width:286px;height:249px;border-radius:3px 3px 0 0}
.match-title{margin-top:26px;text-align:center;font-family:"Roboto Condensed",sans-serif;font-weight:700;font-size:16px;line-height:23px;color:var(--ink);text-transform:uppercase}
.match-text{margin-top:6px;text-align:center;font-size:13.5px;line-height:22px;color:var(--text)}
.read-more{margin:18px auto 0;width:128px;height:34px;border:2px solid var(--ink);border-radius:17px;display:flex;align-items:center;justify-content:center;font-weight:900;font-size:11px;color:var(--ink);text-transform:uppercase}

/* videos */
.video-card{top:2141px;width:446px;height:434px;border:1px solid #dcdcdc;background:var(--white)}
.video-img{width:444px;height:271px;position:relative}
.play{position:absolute;left:50%;top:50%;width:40px;height:40px;margin:-20px 0 0 -20px;border-radius:50%;background:var(--play);border:2px solid var(--white);display:flex;align-items:center;justify-content:center}
.play svg{margin-left:3px}
.video-title{margin-top:34px;text-align:center;font-family:"Roboto Condensed",sans-serif;font-weight:700;font-size:15.5px;line-height:25px;color:var(--ink);text-transform:uppercase}
.video-btn{margin:16px auto 0;width:188px;height:38px;font-size:15px}

/* testimonials */
.testi-band{left:0;top:2654px;width:1200px;height:750px}
.testi-title{top:2776px;color:var(--white);font-weight:700;font-size:37px}
.testi-bar{left:555px;top:2830px;width:90px;height:3px;background:var(--white)}
.testi-card{top:2912px;width:289px;height:256px;background:var(--white);border-top:3px solid var(--blue-bright);border-radius:8px}
.testi-card::after{content:"";position:absolute;left:134px;bottom:-10px;border:10px solid transparent;border-bottom:0;border-top-color:var(--white)}
.quote{position:absolute;left:124px;top:-20px;width:40px;height:40px;border-radius:50%;background:var(--blue);color:var(--white);font-family:"Titillium Web",sans-serif;font-weight:900;font-size:40px;line-height:54px;text-align:center}
.testi-name{margin-top:36px;text-align:center;font-family:"Titillium Web",sans-serif;font-weight:700;font-size:15px;color:var(--blue);text-transform:uppercase}
.testi-text{margin:8px 26px 0;text-align:center;font-size:13.5px;line-height:21px;color:var(--muted)}
.testi-person{top:3196px;width:289px;text-align:center;color:var(--white);font-size:14px}
.stars{top:3219px;width:289px;text-align:center;color:var(--white);font-size:17px;letter-spacing:3px}

/* news */
.news-title{top:3416px;font-weight:700;font-size:37px}
.news-card{top:3525px;width:284px;height:347px;background:var(--white);box-shadow:0 3px 10px rgba(0,0,0,.15)}
.news-img{width:284px;height:182px;position:relative}
.date-tag{position:absolute;left:6px;top:6px;height:24px;padding:0 12px;border-radius:12px;background:var(--blue-bright);color:var(--white);font-weight:900;font-size:11px;display:flex;align-items:center;gap:6px;text-transform:uppercase}
.news-head{margin-top:26px;text-align:center;font-family:"Roboto Condensed",sans-serif;font-weight:700;font-size:16px;color:var(--ink);text-transform:uppercase}
.news-text{margin:10px 30px 0;text-align:center;font-size:13.5px;line-height:21px;color:var(--text)}

/* footer */
.footer{left:0;top:3977px;width:1200px;height:538px;background:var(--footer)}
.foot-head{top:4037px;color:var(--white);font-family:"Titillium Web",sans-serif;font-weight:700;font-size:18px;text-transform:uppercase}
.foot-text{color:#d4d4d4;font-size:14px;line-height:18px}
.contact-row{left:144px;display:flex;gap:14px}
.contact-row svg{flex:none;margin-top:2px}
.email-field{left:438px;top:4130px;width:260px;height:38px;background:var(--white);border:1px solid #ccc;font-size:12px;color:#777;padding:0 12px;display:flex;align-items:center}
.subscribe{left:438px;top:4176px;width:113px;height:37px;background:var(--blue-bright);color:var(--white);font-weight:900;font-size:13px;display:flex;align-items:center;justify-content:center;text-transform:uppercase}
.socials{left:517px;top:4394px;display:flex;gap:11px}
.socials span{width:32px;height:32px;border-radius:50%;border:2px solid var(--white)}
.copyright{left:0;top:4452px;width:1200px;text-align:center;color:#d4d4d4;font-size:14px}
</style>
</head>
<body>

<!-- hero -->
<section class="abs hero" role="img" aria-label="Night stadium photo of soccer players contesting the ball"></section>
<div class="abs hero-photo"></div>
<div class="abs brand"><span class="mark"></span>AGPM</div>
<div class="abs call">
  <svg width="30" height="30" viewBox="0 0 30 30"><circle cx="15" cy="15" r="13.5" fill="none" stroke="#fff" stroke-width="1.6"/><path d="M10.5 8.5l2.5-.5 1.5 3.5-1.6 1.2a8 8 0 0 0 4 4l1.2-1.6 3.5 1.5-.5 2.5c-6 .6-11.2-4.6-10.6-10.6z" fill="#fff"/></svg>
  Call +1 555 0142 7781
</div>
<div class="abs membership">MEMBERSHIP</div>
<nav class="abs nav">
  <span class="active">Home</span><span>About Us</span><span>Our Products</span><span>Sponsors</span><span>Clubs</span><span>Blog</span><span>Contact Us</span>
</nav>
<div class="abs nav-rule"></div>
<h1 class="abs hero-title light">APEX GAME</h1>
<div class="abs hero-title bold">PHOTO MATCHING</div>
<div class="abs btn-pill hero-btn">Find Out More</div>
<div class="abs dots"><span class="on"></span><span></span><span></span><span></span></div>

<!-- welcome -->
<div class="abs heading welcome-kicker">Welcome to</div>
<h2 class="abs heading welcome-title">Apex Game Photo Matching</h2>
<div class="abs bar welcome-bar"></div>
<p class="abs welcome-text">Lorem ipsum dolor sit amet, consectetur adipiscing elit, sed do eiusmod tempor incididunt ut labore et dolore magna aliqua. Ut enim ad minim veniam, quis nostrud exercitation ullamco laboris nisi ut aliquip ex ea commodo consequat. Duis aute irure dolor in reprehenderit in voluptate velit esse cillum dolore eu fugiat nulla pariatur. Excepteur sint occaecat cupidatat non proident, sunt in culpa qui officia deserunt mollit anim id est laborum Sed ut perspiciatis unde omnis iste natus error sit voluptatem accusantium</p>
<div class="abs btn-pill welcome-btn">Learn More</div>
<div class="abs hex" role="img" aria-label="Football player in helmet holding a ball"></div>

<!-- photo matching -->
<div class="abs gray-band"></div>
<div class="abs notch"></div>
<h2 class="abs heading section-title" style="top:1406px">PHOTO MATCHING</h2>
<div class="abs bar center-bar" style="top:1459px"></div>
<p class="abs pm-sub">Lorem ipsum dolor sit amet, consectetur adipiscing elit, sed do eiusmod tempor incididunt ut labore et dolore</p>

<article class="abs match-card" style="left:144px">
  <div class="match-img" role="img" aria-label="Player in red number 9 jersey beside the matched game-worn jersey" style="background:linear-gradient(180deg,#8b8a7a 0%,#a59a7d 40%,#7a3030 70%,#4d5a3a 100%)"></div>
  <h3 class="match-title">Nemo enim ipsam voluptatem<br>quia voluptas</h3>
  <p class="match-text">Lorem ipsum dolor sit amet, consectetur adipiscing elit, sed do eiusmod tempor incididunt ut labore et dolore</p>
  <div class="read-more">Read More</div>
</article>
<article class="abs match-card" style="left:455px">
  <div class="match-img" role="img" aria-label="Football player in red uniform beside the matched game-worn jersey" style="background:linear-gradient(160deg,#8a2a2a 0%,#c4403a 45%,#b03030 70%,#6d2222 100%)"></div>
  <h3 class="match-title">Nemo enim ipsam voluptatem<br>quia voluptas</h3>
  <p class="match-text">Lorem ipsum dolor sit amet, consectetur adipiscing elit, sed do eiusmod tempor incididunt ut labore et dolore</p>
  <div class="read-more">Read More</div>
</article>
<article class="abs match-card" style="left:767px">
  <div class="match-img" role="img" aria-label="Player in red number 9 jersey beside the matched game-worn jersey" style="background:linear-gradient(180deg,#8b8a7a 0%,#a59a7d 40%,#7a3030 70%,#4d5a3a 100%)"></div>
  <h3 class="match-title">Nemo enim ipsam voluptatem<br>quia voluptas</h3>
  <p class="match-text">Lorem ipsum dolor sit amet, consectetur adipiscing elit, sed do eiusmod tempor incididunt ut labore et dolore</p>
  <div class="read-more">Read More</div>
</article>

<!-- videos -->
<article class="abs video-card" style="left:144px">
  <div class="video-img" role="img" aria-label="Video still comparing details of a baseball jersey" style="background:linear-gradient(135deg,#b9b9b6 0%,#8e8f8a 40%,#7a2a2a 75%,#4a4a48 100%)">
    <span class="play"><svg width="12" height="14" viewBox="0 0 12 14"><path d="M0 0l12 7-12 7z" fill="#fff"/></svg></span>
  </div>
  <h3 class="video-title">Nemo enim ipsam voluptatem quia voluptas<br>sit aspernatur aut odit</h3>
  <div class="btn-pill video-btn">Learn More</div>
</article>
<article class="abs video-card" style="left:611px">
  <div class="video-img" role="img" aria-label="Video still comparing a football jersey with game photos" style="background:linear-gradient(90deg,#2a1414 0%,#7a2626 20%,#141414 35%,#b7413a 50%,#141414 65%,#7a2626 80%,#2a1414 100%)">
    <span class="play"><svg width="12" height="14" viewBox="0 0 12 14"><path d="M0 0l12 7-12 7z" fill="#fff"/></svg></span>
  </div>
  <h3 class="video-title">Nemo enim ipsam voluptatem quia voluptas<br>sit aspernatur aut odit</h3>
  <div class="btn-pill video-btn">Learn More</div>
</article>

<!-- testimonials -->
<svg class="abs testi-band" width="1200" height="750" viewBox="0 0 1200 750" role="img" aria-label="Dark stadium photo of soccer players">
  <defs>
    <radialGradient id="stadium" cx="50%" cy="40%" r="70%">
      <stop offset="0" stop-color="#3a4350"/><stop offset=".6" stop-color="#1c2128"/><stop offset="1" stop-color="#0d1013"/>
    </radialGradient>
  </defs>
  <polygon points="0,0 600,40 1200,28 1200,676 600,674 0,712" fill="url(#stadium)"/>
  <polygon points="0,0 600,40 0,44" fill="#2a8fd6"/>
  <polygon points="600,674 1200,676 1200,748" fill="#2a8fd6"/>
</svg>
<h2 class="abs heading section-title testi-title">TESTIMONIALS</h2>
<div class="abs testi-bar"></div>

<article class="abs testi-card" style="left:142px">
  <span class="quote">&ldquo;</span>
  <h3 class="testi-name">Apex Game</h3>
  <p class="testi-text">Sed ut perspiciatis unde omnis iste natus error sit voluptatem accustium doloremque laudantium, totam rem aperiam, eaque ipsa quae ab illo iore veritatis et quasi architecto beatae vitae dicta sunt explicabo. Nemo enim ipsam voluptatem quia</p>
</article>
<article class="abs testi-card" style="left:454px">
  <span class="quote">&ldquo;</span>
  <h3 class="testi-name">Apex Game</h3>
  <p class="testi-text">Sed ut perspiciatis unde omnis iste natus error sit voluptatem accustium doloremque laudantium, totam rem aperiam, eaque ipsa quae ab illo iore veritatis et quasi architecto beatae vitae dicta sunt explicabo. Nemo enim ipsam voluptatem quia</p>
</article>
<article class="abs testi-card" style="left:764px">
  <span class="quote">&ldquo;</span>
  <h3 class="testi-name">Apex Game</h3>
  <p class="testi-text">Sed ut perspiciatis unde omnis iste natus error sit voluptatem accustium doloremque laudantium, totam rem aperiam, eaque ipsa quae ab illo iore veritatis et quasi architecto beatae vitae dicta sunt explicabo. Nemo enim ipsam voluptatem quia</p>
</article>
<div class="abs testi-person" style="left:142px">Dana Morrow</div>
<div class="abs testi-person" style="left:454px">Dana Morrow</div>
<div class="abs testi-person" style="left:764px">Dana Morrow</div>
<div class="abs stars" style="left:142px">★★★★★</div>
<div class="abs stars" style="left:454px">★★★★★</div>
<div class="abs stars" style="left:764px">★★★★★</div>

<!-- news -->
<h2 class="abs heading section-title news-title">LATEST NEWS</h2>
<article class="abs news-card" style="left:144px">
  <div class="news-img" role="img" aria-label="Blue and white soccer jerseys front and back" style="background:linear-gradient(90deg,#e8ecf3 0%,#2c4a9a 30%,#f1f3f7 50%,#1f3a86 75%,#e8ecf3 100%)">
    <span class="date-tag"><svg width="10" height="10" viewBox="0 0 10 10"><rect x=".5" y="1.5" width="9" height="8" fill="none" stroke="#fff"/><rect x=".5" y="1.5" width="9" height="2.5" fill="#fff"/></svg>Oct 17, 2020</span>
  </div>
  <h3 class="news-head">Quis autem vel eum iure</h3>
  <p class="news-text">Sed ut perspiciatis unde omnis iste natus error sit voluptatem accusantium doloque lauantium, totam rem aperiam,</p>
</article>
<article class="abs news-card" style="left:459px">
  <div class="news-img" role="img" aria-label="Football player in gold helmet holding a ball" style="background:radial-gradient(circle at 50% 45%,#9c7a3a 0%,#3e3422 40%,#0d0d0d 80%)">
    <span class="date-tag"><svg width="10" height="10" viewBox="0 0 10 10"><rect x=".5" y="1.5" width="9" height="8" fill="none" stroke="#fff"/><rect x=".5" y="1.5" width="9" height="2.5" fill="#fff"/></svg>Oct 17, 2020</span>
  </div>
  <h3 class="news-head">Quis autem vel eum iure</h3>
  <p class="news-text">Sed ut perspiciatis unde omnis iste natus error sit voluptatem accusantium doloque lauantium, totam rem aperiam,</p>
</article>
<article class="abs news-card" style="left:773px">
  <div class="news-img" role="img" aria-label="Soccer player in red kit on a stadium pitch" style="background:linear-gradient(180deg,#c69a6a 0%,#a86a4a 35%,#c0332e 60%,#4f7a3a 100%)">
    <span class="date-tag"><svg width="10" height="10" viewBox="0 0 10 10"><rect x=".5" y="1.5" width="9" height="8" fill="none" stroke="#fff"/><rect x=".5" y="1.5" width="9" height="2.5" fill="#fff"/></svg>Oct 17, 2020</span>
  </div>
  <h3 class="news-head">Quis autem vel eum iure</h3>
  <p class="news-text">Sed ut perspiciatis unde omnis iste natus error sit voluptatem accusantium doloque lauantium, totam rem aperiam,</p>
</article>

<!-- footer -->
<footer class="abs footer"></footer>
<h4 class="abs foot-head" style="left:144px">Contact Us</h4>
<h4 class="abs foot-head" style="left:438px">Sign Up for Newsletter</h4>
<h4 class="abs foot-head" style="left:769px">About AGPM</h4>

<div class="abs contact-row" style="top:4087px">
  <svg width="16" height="20" viewBox="0 0 16 20"><path d="M8 1a6 6 0 0 0-6 6c0 4.5 6 11.5 6 11.5S14 11.5 14 7a6 6 0 0 0-6-6z" fill="none" stroke="#ddd" stroke-width="1.4"/><circle cx="8" cy="7" r="2" fill="#ddd"/></svg>
  <p class="foot-text">Apex Game Photo Matching<br>4120 Harbor Crest Ave.<br>Lakeview, CA 90000</p>
</div>
<div class="abs contact-row" style="top:4162px">
  <svg width="16" height="16" viewBox="0 0 16 16"><path d="M3 1.5l3 .2 1.2 3.4-1.8 1.3a8 8 0 0 0 4.2 4.2l1.3-1.8 3.4 1.2.2 3C7.5 13.5 2.5 8.5 3 1.5z" fill="none" stroke="#ddd" stroke-width="1.3"/></svg>
  <p class="foot-text">Phone:<br>555-0193-2208</p>
</div>
<div class="abs contact-row" style="top:4217px">
  <svg width="16" height="14" viewBox="0 0 16 14"><rect x="1" y="2" width="14" height="10" fill="none" stroke="#ddd" stroke-width="1.3"/><path d="M1 2l7 6 7-6" fill="none" stroke="#ddd" stroke-width="1.3"/></svg>
  <p class="foot-text">E-mail:<br>hello@apexgamematch.test</p>
</div>

<p class="abs foot-text" style="left:438px;top:4093px">Sign up to our mailing list</p>
<div class="abs email-field">Enter email</div>
<div class="abs subscribe">Subscribe</div>

<p class="abs foot-text" style="left:769px;top:4084px;width:290px;font-size:13.5px;line-height:20px">Nemo enim ipsam voluptatem quia voluptas sit aspernatur aut odit aut fugit, sed quia consequuntur magni dolores eos qui ratione voluptatem sequi nesciunt. Neque porro quisquam est, qui dolorem ipsum quia dolor sit amet, consectetur, adipisci velit, sed quia non numquam</p>

<div class="abs socials"><span></span><span></span><span></span><span></span></div>
<p class="abs copyright">(c) 2020 Apex Game Photo Matching | All Rights Reserved | Disclaimer</p>

</body>
</html>
```